Quorvane - corporate Business Card

We need a good look and innovative business card for a new start up company based in Los Angeles called "Quorvane". We are in a payment business, including payment card, app, and ewallet. We are expert in online payment and Card not present (CNP) transaction.
We need an innovative, modern business card.

Our logo font is Aero Matics

Target Market(s)

Startup - Bank - Online Payment - Card Manufacturing

Industry/Entity Type

Startup

Contact Information for Business Card

phone: 424 555 0173 - Address: 4270 Marbrook blvd, Cylver City, CA 90232

Requirements
Must have
• Message: innovative, professional, expert, high tech, trust, online payment expert, security
Nice to have
• no comment
Should not have
• no Comment

```html
<!DOCTYPE html>
<html lang="en">
<head>
<meta charset="utf-8">
<title>Quorvane — Business Card</title>
<link rel="stylesheet" href="https://fonts.googleapis.com/css2?family=Exo+2:wght@400;500;600&display=swap">
<style>
  :root {
    --canvas: #ececec;
    --red: #d42a38;
    --red-dark: #a8121f;
    --red-light: #e9505b;
    --slate: #3b434e;
    --white: #ffffff;
    --ink: #4a4a4a;
    --globe: #e4e4e4;
  }
  * { box-sizing: border-box; margin: 0; padding: 0; }
  html, body { width: 1200px; height: 800px; overflow: hidden; }
  body {
    background: var(--canvas);
    font-family: "Exo 2", sans-serif;
    position: relative;
  }
  .card {
    position: absolute;
    top: 246px;
    width: 540px;
    height: 309px;
    overflow: hidden;
    box-shadow: 0 10px 30px rgba(0,0,0,0.12);
  }
  .card--front { left: 50px; background: var(--red); }
  .card--back { left: 610px; background: var(--white); }
  .card__art { position: absolute; inset: 0; width: 100%; height: 100%; }

  .brand {
    position: absolute;
    display: flex;
    align-items: center;
    gap: 12px;
    font-weight: 600;
    letter-spacing: 1px;
    white-space: nowrap;
  }
  .brand__dot { border-radius: 50%; flex: none; }
  .brand--front { left: 160px; top: 116px; color: var(--white); font-size: 44px; }
  .brand--front .brand__dot { width: 58px; height: 58px; background: var(--white); }
  .brand--back { left: 330px; top: 44px; color: var(--red); font-size: 26px; gap: 10px; }
  .brand--back .brand__dot { width: 32px; height: 32px; background: var(--red); }

  .holder { position: absolute; left: 96px; top: 28px; color: var(--white); white-space: nowrap; }
  .holder__name { font-size: 32px; font-weight: 600; letter-spacing: 1px; }
  .holder__role { font-size: 16px; font-weight: 400; letter-spacing: 2px; margin-top: -2px; }

  .web { position: absolute; left: 14px; top: 188px; display: flex; align-items: center; gap: 10px;
         color: var(--red); font-size: 10px; }
  .web__dot { width: 14px; height: 14px; border-radius: 50%; background: var(--red); }

  .contact { position: absolute; left: 316px; top: 0; list-style: none; color: var(--ink); font-size: 9px; }
  .contact li { position: absolute; left: 0; white-space: nowrap; }
  .contact__address { top: 144px; }
  .contact__phone { top: 184px; }
  .contact__email { top: 224px; }
</style>
</head>
<body>

<section class="card card--front" aria-label="Card front">
  <svg class="card__art" viewBox="0 0 540 309">
    <defs>
      <radialGradient id="front-globe" cx="0.45" cy="0.45" r="0.6">
        <stop offset="0" stop-color="#e23a47"/>
        <stop offset="1" stop-color="#b8192a"/>
      </radialGradient>
    </defs>
    <rect width="540" height="309" fill="var(--red)"/>
    <g role="img" aria-label="World map globe over a red network grid illustration">
      <circle cx="250" cy="170" r="250" fill="url(#front-globe)" opacity="0.75"/>
    </g>
    <polygon points="190,300 540,300 540,309 182,309" fill="var(--slate)"/>
  </svg>
  <div class="brand brand--front"><span class="brand__dot"></span>quorvane</div>
</section>

<section class="card card--back" aria-label="Card back">
  <svg class="card__art" viewBox="0 0 540 309">
    <defs>
      <radialGradient id="back-globe" cx="0.5" cy="0.5" r="0.5">
        <stop offset="0" stop-color="#f4f4f4"/>
        <stop offset="1" stop-color="var(--globe)"/>
      </radialGradient>
      <radialGradient id="panel-globe" cx="0.5" cy="0.5" r="0.5">
        <stop offset="0" stop-color="#c71e2d"/>
        <stop offset="1" stop-color="#b51525"/>
      </radialGradient>
      <clipPath id="panel-clip">
        <polygon points="0,0 330,0 240,176 0,176"/>
      </clipPath>
    </defs>
    <g role="img" aria-label="Faint world globe illustration">
      <circle cx="420" cy="80" r="80" fill="url(#back-globe)"/>
    </g>
    <polygon points="0,0 330,0 240,176 0,176" fill="var(--red)"/>
    <g role="img" aria-label="World map over red network grid illustration" clip-path="url(#panel-clip)">
      <circle cx="150" cy="140" r="120" fill="url(#panel-globe)" opacity="0.7"/>
    </g>
    <line x1="0" y1="214" x2="200" y2="214" stroke="var(--red)" stroke-width="4"/>
    <line x1="296" y1="130" x2="232" y2="258" stroke="var(--red)" stroke-width="40" stroke-linecap="round"/>
    <g fill="none" stroke="var(--white)" stroke-width="2" stroke-linejoin="round" stroke-linecap="round">
      <path class="icon-home" d="M274 152 L284 143 L294 152 M277 150 V160 H291 V150"/>
      <path class="icon-phone" d="M257 183 c-2 4 2 12 8 14 l3 -3 -3 -3 -2 1 c-2 -1 -4 -4 -4 -6 l2 -1 -1 -4 z"/>
      <rect class="icon-mail" x="236" y="223" width="18" height="12"/>
      <path class="icon-mail" d="M236 223 L245 230 L254 223"/>
    </g>
    <polygon points="330,300 540,300 540,309 324,309" fill="var(--slate)"/>
  </svg>

  <div class="holder">
    <p class="holder__name">Mr. Talbren</p>
    <p class="holder__role">managing director</p>
  </div>

  <div class="web"><span class="web__dot"></span>www.quorvane.com</div>

  <ul class="contact">
    <li class="contact__address">4270 Marbrook blvd, Cylver City, CA 90232</li>
    <li class="contact__phone">424 555 0173</li>
    <li class="contact__email">hello@quorvane.com</li>
  </ul>

  <div class="brand brand--back"><span class="brand__dot"></span>quorvane</div>
</section>

</body>
</html>
```